Bref créative
Stationary for Visual Explanation Business
Bus Card, Stationary
Professional
Martin Pelloway
CEO & Founder
487 E 29th Street, Suite 4B
New York, NY 10027
USA
martin@lumbrivista.com
www.lumbrivista.com
Looking for clean and modern sophisticated look and feel for a marketing service business company that offers visual explanations for technology companies. Not cutesy. A blend of QXR combined with creative agency.
The letterhead will serve as my proposal template. I will use it for placing text and illustrations.
I want to keep with the orange and gray of the logo.
I wil supply the AI version of the logo shortly.
Logo AI File with tagline and name
Logo Ai File with company name and no tagline
Logo Ai file with no tagline and no company name

```html
<!DOCTYPE html>
<html lang="en">
<head>
<meta charset="utf-8">
<title>Lumbrivista – Business Card</title>
<link rel="stylesheet" href="https://fonts.googleapis.com/css2?family=PT+Sans:wght@400;700&display=swap">
<style>
  :root {
    --paper: #ffffff;
    --trim: #1a1a1a;
    --orange: #f7941d;
    --slate: #5f6062;
    --band-gray: #c9c9c9;
    --chip-peach: #fddcbd;
    --chip-gray: #d0d0d0;
  }
  * { margin: 0; padding: 0; box-sizing: border-box; }
  html, body {
    width: 1200px; height: 751px; overflow: hidden;
    background: var(--paper);
    font-family: "PT Sans", Arial, sans-serif;
  }
  .canvas { position: relative; width: 1200px; height: 751px; }
  .card-edge {
    position: absolute; left: 72px; top: 77px;
    width: 1056px; height: 600px;
    border: 2px solid var(--trim);
  }
  .brand-name {
    position: absolute; left: 149px; top: 318px;
    font-size: 60px; line-height: 64px; font-weight: 700;
    color: var(--slate); letter-spacing: -0.5px;
  }
  .contact { position: absolute; left: 727px; top: 208px; color: var(--slate); font-weight: 700; }
  .contact-name { font-size: 42px; color: var(--orange); line-height: 48px; }
  .contact-role { font-size: 33px; line-height: 40px; }
  .contact-details { margin-top: 44px; font-size: 27px; line-height: 35px; }
  .band { position: absolute; top: 619px; height: 25px; }
  .band-long { left: 72px; width: 785px; background: var(--band-gray); }
  .chip-peach { background: var(--chip-peach); }
  .chip-gray { background: var(--chip-gray); }
</style>
</head>
<body>
<div class="canvas">
  <div class="card-edge"></div>

  <div class="brand-name">Lumbrivista</div>

  <div class="contact">
    <div class="contact-name">Martin Pelloway</div>
    <div class="contact-role">CEO &amp; Founder</div>
    <div class="contact-details">
      <div>487 E 29th Street, Suite 4B</div>
      <div>New York, NY 10027</div>
      <div>Phone: (917) 555-0148</div>
      <div>martin@lumbrivista.com</div>
      <div>www.lumbrivista.com</div>
    </div>
  </div>

  <div class="band band-long"></div>
  <div class="band chip-peach" style="left:871px;width:37px"></div>
  <div class="band chip-gray" style="left:922px;width:38px"></div>
  <div class="band chip-peach" style="left:974px;width:39px"></div>
  <div class="band chip-gray" style="left:1027px;width:39px"></div>
  <div class="band chip-peach" style="left:1080px;width:43px"></div>
</div>
</body>
</html>
```